I would like to design a flyer that I can put on car windows, inside peoples mailboxes. This flyer is to display Vantor Athletics and Wellness is now Open. I would like this to be a Free One Week Pass! I would like to have the following information on the flyer.
1) My logo - VANTOR ATHLETICS AND WELLNESS (I will upload the logo)
2) Hours of operation - Mon - Fri "5am - 10pm" Sat/Sun "6am -6pm"
3) Membership $59.00 "No Initiation Fee" Month to Month Membership.
Class are free. The Classes are Yoga, Salsa Classes, Bootcamps, HITT, Sports Performance,
4) Personal Training
5) Message Therapy
6) Address: 2718 Marwick Commerce Dr. Suite 312
Chantilly, VA 20987
7) mail@vantoranw.example
8) Free One Week Pass

```html
<!DOCTYPE html>
<html lang="en">
<head>
<meta charset="utf-8">
<title>Vantor Athletics and Wellness – Free One Week Pass Flyer</title>
<link rel="stylesheet" href="https://fonts.googleapis.com/css2?family=Josefin+Sans:wght@400;600;700&family=Delius&display=swap">
<style>
  :root {
    --brand-red: #d71f27;
    --charcoal: #474747;
    --charcoal-dark: #3a3a3a;
    --paper: #ffffff;
    --ring-grey: #c9c9cc;
    --ring-navy: #4a4d5c;
    --ink: #3b3b3b;
  }
  html, body {
    margin: 0;
    padding: 0;
    width: 1022px;
    height: 1200px;
    overflow: hidden;
    background: var(--paper);
  }
  .flyer { display: block; width: 1022px; height: 1200px; }
  .headline { font-family: "Josefin Sans", sans-serif; font-weight: 700; }
  .label { font-family: "Josefin Sans", sans-serif; font-weight: 600; }
  .body-text { font-family: "Josefin Sans", sans-serif; font-weight: 400; }
  .hours-text { font-family: "Delius", sans-serif; }
  .fill-red { fill: var(--brand-red); }
  .fill-white { fill: var(--paper); }
  .fill-ink { fill: var(--ink); }
</style>
</head>
<body>
<svg class="flyer" viewBox="0 0 1022 1200" xmlns="http://www.w3.org/2000/svg">
  <defs>
    <linearGradient id="photo-lifter" x1="0" y1="0" x2="1" y2="1">
      <stop offset="0" stop-color="#2a2e33"/>
      <stop offset="0.6" stop-color="#7a6a5e"/>
      <stop offset="1" stop-color="#1c1c1c"/>
    </linearGradient>
    <linearGradient id="photo-trainer" x1="0" y1="0" x2="1" y2="1">
      <stop offset="0" stop-color="#6b6a6c"/>
      <stop offset="0.5" stop-color="#9a7f80"/>
      <stop offset="1" stop-color="#3c5a78"/>
    </linearGradient>
    <linearGradient id="photo-class" x1="0" y1="0" x2="1" y2="1">
      <stop offset="0" stop-color="#8a7a6c"/>
      <stop offset="0.5" stop-color="#5e5048"/>
      <stop offset="1" stop-color="#3a3a42"/>
    </linearGradient>
  </defs>

  <!-- background panels -->
  <rect class="fill-white" width="1022" height="1200"/>
  <polygon class="fill-red" points="0,0 322,0 0,1010"/>
  <polygon style="fill:var(--charcoal)" points="300,0 355,0 290,155 235,155"/>
  <polygon class="fill-red" points="385,0 445,0 418,80 358,80"/>
  <polygon style="fill:var(--charcoal)" points="0,470 230,330 1022,1200 0,1200"/>
  <polygon class="fill-red" points="92,620 118,620 18,900 0,900 0,860"/>
  <polygon class="fill-white" points="100,632 162,632 117,718 58,718"/>

  <!-- decorative rings -->
  <circle cx="925" cy="40" r="92" fill="none" stroke="var(--ring-grey)" stroke-width="7"/>
  <circle cx="925" cy="40" r="66" fill="none" stroke="var(--ring-navy)" stroke-width="6"/>
  <circle cx="232" cy="410" r="135" fill="none" stroke="var(--ring-grey)" stroke-width="5"/>
  <circle cx="445" cy="700" r="150" fill="none" stroke="var(--ring-grey)" stroke-width="5"/>
  <circle cx="445" cy="700" r="136" fill="none" stroke="var(--ring-navy)" stroke-width="4"/>

  <!-- photo circle: lifter -->
  <g class="photo-badge">
    <circle cx="135" cy="308" r="135" style="fill:var(--charcoal-dark)"/>
    <path class="fill-red" d="M0,308 A135,135 0 0 0 270,308 Z"/>
    <circle cx="135" cy="308" r="108" fill="url(#photo-lifter)" role="img" aria-label="Photo of a muscular athlete lifting a dumbbell"/>
  </g>

  <!-- photo circle: trainer -->
  <g class="photo-badge">
    <circle cx="357" cy="535" r="142" style="fill:var(--charcoal)"/>
    <circle cx="357" cy="535" r="132" fill="none" stroke="var(--paper)" stroke-width="2"/>
    <path class="fill-red" d="M232,535 A125,125 0 0 0 482,535 Z"/>
    <circle cx="357" cy="535" r="108" fill="url(#photo-trainer)" role="img" aria-label="Photo of a personal trainer coaching a client in the gym"/>
  </g>

  <!-- photo circle: class -->
  <g class="photo-badge">
    <circle cx="660" cy="855" r="262" style="fill:var(--charcoal)"/>
    <circle cx="660" cy="855" r="248" fill="none" stroke="var(--paper)" stroke-width="2"/>
    <path class="fill-red" d="M420,855 A240,240 0 0 0 900,855 Z"/>
    <circle cx="660" cy="855" r="212" fill="url(#photo-class)" role="img" aria-label="Photo of a trainer helping a member with sit-ups in a studio class"/>
  </g>

  <!-- offer -->
  <g class="offer">
    <text class="headline fill-white" x="135" y="100" font-size="68" text-anchor="middle">FREE</text>
    <text class="label fill-white" x="135" y="132" font-size="28" text-anchor="middle">ONE WEEK</text>
    <text class="headline fill-white" x="135" y="182" font-size="60" text-anchor="middle">PASS</text>
  </g>

  <!-- brand -->
  <g class="brand">
    <circle class="fill-red" cx="432" cy="178" r="72"/>
    <text class="headline fill-red" x="992" y="206" font-size="84" text-anchor="end">VANTOR</text>
    <text class="label fill-ink" x="992" y="246" font-size="20" letter-spacing="4" text-anchor="end">ATHLETICS AND WELLNESS</text>
  </g>

  <!-- services -->
  <g class="services">
    <text class="label fill-ink" x="992" y="326" font-size="44" text-anchor="end">MESSAGE THERAPY</text>
    <text class="label fill-ink" x="992" y="376" font-size="44" text-anchor="end">PERSONAL TRAINING</text>
  </g>

  <!-- hours -->
  <g class="hours">
    <polygon class="fill-red" points="428,410 1022,410 1022,462 478,462"/>
    <text class="label fill-white" x="992" y="448" font-size="30" text-anchor="end">HOURS OF OPERATION</text>
    <text class="hours-text fill-ink" x="992" y="504" font-size="28" text-anchor="end">Monday to Friday</text>
    <text class="hours-text fill-red" x="992" y="542" font-size="32" text-anchor="end">5am-10pm</text>
    <text class="hours-text fill-ink" x="992" y="584" font-size="28" text-anchor="end">Saturday/Sunday</text>
    <text class="hours-text fill-red" x="992" y="622" font-size="32" text-anchor="end">6am-6pm</text>
  </g>

  <!-- membership -->
  <g class="membership">
    <text class="body-text fill-white" x="31" y="776" font-size="22">Membership</text>
    <text class="label fill-white" x="31" y="842" font-size="64">$59.00</text>
    <rect class="fill-white" x="31" y="862" width="305" height="3"/>
    <text class="body-text fill-white" x="31" y="892" font-size="21">"No Initiation Fee"</text>
    <text class="label fill-white" x="31" y="916" font-size="19">MONTH TO MONTH</text>
    <text class="label fill-white" x="31" y="940" font-size="19">MEMBERSHIP.</text>
    <rect class="fill-white" x="31" y="958" width="305" height="3"/>
    <text class="label fill-white" x="31" y="992" font-size="28">CLASS ARE FREE.</text>
    <text class="label fill-white" x="31" y="1020" font-size="19">THE CLASSES ARE YOGA,</text>
    <text class="label fill-white" x="31" y="1044" font-size="19">SALSA CLASSES, BOOTCAMPS,</text>
    <text class="label fill-white" x="31" y="1068" font-size="19">HITT, SPORTS PERFORMANCE,</text>
  </g>

  <!-- footer -->
  <g class="contact">
    <rect class="fill-white" x="0" y="1086" width="895" height="4"/>
    <text class="body-text fill-white" x="480" y="1126" font-size="19" text-anchor="middle">2718 Marwick Commerce Dr. Suite 312, Chantilly, VA 20987</text>
    <text class="body-text fill-white" x="480" y="1154" font-size="19" text-anchor="middle">703-555-0148 | mail@vantoranw.example</text>
  </g>
</svg>
</body>
</html>
```